Popup Nightclub Grand Opening Flyer

We need to design a flyer for the grand opening of an upscale, exclusive nightclub called "Lanternfall". The design needs to be chic and exclusive. The background should be black and the text should primarily be white. We like minimalist designs.

Here is the text for the flyer
-
Velvetrope Atlanta Presents

Lanternfall (LOGO)

A Popup Nightclub Experience
For one night Only

Friday, October 18, 2013
Party begins at 9PM

INVITE ONLY

See invitation for location details
(Velvetrope Atlanta logo)

-
Examples we like

http://cdn2-b.brivelpost.com/sites/default/files/styles/image_content_width/hash/3d/fa/1472093815_4471_flyer.jpg?itok=R8kqWm2z

http://api.plovra.com/files/7Kqq-Tr82XXB3pQzJvmtR5HL2W719E4nbRtC6KLd4HsfM8Y2qTDK-VmjwDoNqLX4QBzTHD9nakRbVx3m-Pfq8htc3MDTWr5p4/2zelSaturdays.jpg

http://quenmar.com/wp-content/uploads/yootheme/widgetkit/gallery/2zel/2zel-gen_vroom4-01.jpg

Hi All, one thing that we are seeing that we don't like is on over emphasis on the phrase "a popup nightclub experience" please don't make this the largest thing on the flyer

Target Market(s)

Target market is 25-35 year olds who are affluent (rich) and like luxury brands

Requirements
Must have
• Dark Background
Nice to have
• Velvetrope Logo on the bottom
Modern text that isn't curvy
Should not have
• Curved text

```html
<!DOCTYPE html>
<html lang="en">
<head>
<meta charset="utf-8">
<title>Lanternfall Nightclub – Velvetrope Atlanta</title>
<link href="https://fonts.googleapis.com/css2?family=Josefin+Sans:wght@300;400&family=Open+Sans:wght@400;700;800&display=swap" rel="stylesheet">
<style>
  :root {
    --ink: #0d0e0f;
    --stone: #2b2d2e;
    --stone-light: #5a5c5d;
    --teal-haze: rgba(38, 78, 84, 0.55);
    --white: #f4f4f4;
    --soft-white: #dcdcdc;
    --gold: #f2e59a;
    --date-fill: #1d3b37;
    --ring: #9a9c9d;
    --badge-fill: #9d9e9f;
  }
  html, body {
    margin: 0;
    padding: 0;
    width: 851px;
    height: 1200px;
    overflow: hidden;
    background: var(--ink);
  }
  .flyer {
    position: relative;
    width: 851px;
    height: 1200px;
    overflow: hidden;
    background:
      radial-gradient(ellipse 55% 40% at 38% 48%, var(--teal-haze), transparent 70%),
      radial-gradient(ellipse 45% 35% at 70% 30%, rgba(70, 74, 76, 0.45), transparent 70%),
      radial-gradient(ellipse 80% 75% at 50% 50%, var(--stone) 0%, #1b1c1d 60%, transparent 100%),
      linear-gradient(90deg, var(--stone-light) 0%, #1a1b1c 6%, #1a1b1c 94%, var(--stone-light) 100%);
    font-family: "Open Sans", Arial, sans-serif;
    color: var(--white);
  }
  .presenter {
    position: absolute;
    left: 68px;
    top: 56px;
    margin: 0;
    font-size: 26px;
    font-weight: 400;
    color: var(--white);
  }
  .presenter .host { color: var(--gold); }

  .club-mark {
    position: absolute;
    left: 396px;
    top: 150px;
    width: 60px;
    height: 60px;
    border: 3px solid var(--soft-white);
    border-radius: 50%;
    box-sizing: border-box;
  }
  .club-name {
    position: absolute;
    left: 0;
    width: 851px;
    top: 300px;
    margin: 0;
    text-align: center;
    font-family: "Josefin Sans", "Helvetica Neue", sans-serif;
    font-weight: 300;
    color: var(--white);
    line-height: 1;
  }
  .club-name .word {
    display: block;
    font-size: 78px;
    letter-spacing: 10px;
  }
  .club-name .kind {
    display: block;
    margin-top: 14px;
    font-size: 40px;
    letter-spacing: 8px;
  }
  .tagline {
    position: absolute;
    left: 0;
    width: 851px;
    top: 462px;
    margin: 0;
    text-align: center;
    font-size: 16px;
    font-weight: 700;
    letter-spacing: 2.4px;
    word-spacing: 3px;
  }
  .tagline-rule {
    position: absolute;
    left: 324px;
    top: 503px;
    width: 204px;
    height: 1px;
    background: linear-gradient(90deg, transparent, var(--soft-white), transparent);
  }
  .date-badge {
    position: absolute;
    left: 92px;
    top: 512px;
    width: 220px;
    height: 220px;
    border-radius: 50%;
    box-sizing: border-box;
    border: 7px solid var(--ring);
    background: radial-gradient(circle at 50% 45%, #28504a, var(--date-fill) 70%);
    box-shadow: 0 0 0 2px #3a3b3c;
    display: flex;
    flex-direction: column;
    align-items: center;
    justify-content: center;
    color: var(--gold);
    font-weight: 400;
    line-height: 1.15;
    text-align: center;
  }
  .date-badge .day { font-size: 32px; letter-spacing: 1px; }
  .date-badge .month { font-size: 32px; }
  .date-badge .year { font-size: 36px; }

  .access {
    position: absolute;
    left: 348px;
    top: 640px;
    margin: 0;
    font-size: 17px;
    font-weight: 700;
    letter-spacing: 4.5px;
    color: var(--soft-white);
  }
  .glass-art {
    position: absolute;
    left: 528px;
    top: 590px;
    width: 236px;
    height: 316px;
    background: linear-gradient(180deg, rgba(60, 62, 64, 0.55), rgba(25, 26, 27, 0.75));
    clip-path: polygon(0 0, 100% 0, 92% 100%, 8% 100%);
  }
  .time-badge {
    position: absolute;
    left: 580px;
    top: 634px;
    width: 164px;
    height: 164px;
    border-radius: 50%;
    box-sizing: border-box;
    background: var(--white);
    padding: 8px;
  }
  .time-badge .inner {
    width: 100%;
    height: 100%;
    border-radius: 50%;
    box-sizing: border-box;
    border: 6px solid #1a1a1a;
    background: var(--badge-fill);
    display: flex;
    flex-direction: column;
    align-items: center;
    justify-content: center;
    color: #111;
    text-align: center;
  }
  .time-badge .lead {
    font-size: 12px;
    font-weight: 700;
    letter-spacing: 1px;
  }
  .time-badge .hour {
    font-size: 34px;
    font-weight: 800;
    line-height: 1.1;
  }
  .location-note {
    position: absolute;
    left: 0;
    width: 851px;
    top: 929px;
    margin: 0;
    text-align: center;
    font-family: Arial, "Helvetica Neue", sans-serif;
    font-size: 24px;
    color: var(--white);
  }
  .host-mark {
    position: absolute;
    left: 170px;
    top: 1012px;
    display: flex;
    align-items: center;
    gap: 22px;
  }
  .host-mark .dot {
    width: 62px;
    height: 62px;
    border-radius: 50%;
    border: 3px solid var(--white);
    box-sizing: border-box;
  }
  .host-mark .divider {
    width: 2px;
    height: 72px;
    background: var(--white);
  }
  .host-mark .name {
    font-family: "Josefin Sans", "Helvetica Neue", sans-serif;
    font-weight: 400;
    color: var(--white);
    line-height: 1;
  }
  .host-mark .name .big {
    display: block;
    font-size: 50px;
    letter-spacing: 6px;
  }
  .host-mark .name .small {
    display: block;
    margin-top: 8px;
    font-size: 20px;
    letter-spacing: 6px;
  }
</style>
</head>
<body>
  <main class="flyer">
    <p class="presenter"><span class="host">Velvetrope Atlanta</span> Presents</p>

    <div class="club-mark" aria-hidden="true"></div>
    <h1 class="club-name">
      <span class="word">LANTERNFALL</span>
      <span class="kind">NIGHTCLUB</span>
    </h1>

    <p class="tagline">A Popup Nightclub Experience&nbsp; For one night Only</p>
    <div class="tagline-rule"></div>

    <div class="date-badge">
      <span class="day">FRIDAY</span>
      <span class="month">OCTOBER 18</span>
      <span class="year">2013</span>
    </div>

    <p class="access">INVITE ONLY</p>

    <div class="glass-art" role="img" aria-label="Dark glass tumbler illustration"></div>
    <div class="time-badge">
      <div class="inner">
        <span class="lead">PARTY BEGINS AT</span>
        <span class="hour">9PM</span>
      </div>
    </div>

    <p class="location-note">See invitation for location details</p>

    <div class="host-mark">
      <span class="dot" aria-hidden="true"></span>
      <span class="divider" aria-hidden="true"></span>
      <span class="name">
        <span class="big">VELVETROPE</span>
        <span class="small">ATLANTA</span>
      </span>
    </div>
  </main>
</body>
</html>
```